Webdesign für Stahl- und Brückenbauunternehmen
Zielgruppe
Wir haben 180 Jahre Erfahrung im Stahl- und Brückenbau.
Unsere Auftraggeber ist die öffentliche Hand.
Aufgabenstellung
Das ODLA / TKU-Logo soll mit rein (siehe jetzige Webseite)

```html
<!DOCTYPE html>
<html lang="de">
<head>
<meta charset="utf-8">
<title>RVB – Leistungen</title>
<link href="https://fonts.googleapis.com/css2?family=Nunito:wght@800&family=Didact+Gothic&display=swap" rel="stylesheet">
<style>
  :root {
    --blue: #0079c2;
    --dark: #2a2a2f;
    --page: #f5f6fa;
    --white: #ffffff;
    --ink: #222228;
    --line: rgba(255,255,255,0.22);
  }
  * { box-sizing: border-box; margin: 0; padding: 0; }
  html, body { width: 1200px; height: 3291px; overflow: hidden; }
  body { background: var(--page); font-family: "Didact Gothic", sans-serif; color: var(--ink); position: relative; }
  .topbar { position: absolute; left: 0; top: 0; width: 1200px; height: 21px; background: var(--blue); }
  .header { position: absolute; left: 0; top: 21px; width: 1200px; height: 285px; border-bottom: 2px solid #d9dbe0; }
  .brand { position: absolute; left: 75px; top: 90px; font-family: "Nunito", sans-serif; font-weight: 800; font-size: 150px; line-height: 1; color: var(--blue); letter-spacing: -4px; }
  .menu-button { position: absolute; left: 966px; top: 74px; width: 150px; height: 150px; border-radius: 22px; background: var(--blue); }
  .menu-button span { position: absolute; left: 36px; width: 78px; height: 12px; background: var(--white); }
  .nav { position: absolute; left: 0; top: 339px; width: 1200px; z-index: 2; }
  .nav-item { display: flex; align-items: center; justify-content: space-between; height: 210px; margin-bottom: 6px; padding: 0 78px 0 94px; background: var(--blue); color: var(--white); font-family: "Nunito", sans-serif; font-weight: 800; font-size: 50px; letter-spacing: 1px; }
  .nav-item svg { width: 100px; height: 100px; }
  .section-title { position: absolute; left: 82px; top: 1160px; font-family: "Nunito", sans-serif; font-weight: 800; font-size: 64px; letter-spacing: 3px; z-index: 1; }
  .intro { position: absolute; left: 84px; top: 1262px; width: 760px; font-size: 38px; line-height: 71px; letter-spacing: 1px; }
  .card { position: absolute; left: 82px; width: 1002px; height: 668px; border-radius: 24px; color: var(--white); }
  .card.blue { background: var(--blue); }
  .card.dark { background: var(--dark); }
  .card-head { position: absolute; left: 60px; top: 64px; display: flex; align-items: center; }
  .icon-tile { width: 161px; height: 160px; border-radius: 18px; background: var(--white); display: flex; align-items: center; justify-content: center; }
  .icon-tile .mark { width: 94px; height: 84px; background: #2e2e33; border-radius: 6px; }
  .card-title { margin-left: 76px; font-family: "Nunito", sans-serif; font-weight: 800; font-size: 57px; letter-spacing: 1px; }
  .divider { position: absolute; left: 54px; top: 264px; width: 881px; height: 2px; background: var(--line); }
  .card-text { position: absolute; left: 65px; top: 290px; width: 900px; font-size: 45px; line-height: 75px; letter-spacing: 0.5px; }
</style>
</head>
<body>
  <div class="topbar"></div>
  <header class="header">
    <div class="brand">RVB</div>
    <div class="menu-button">
      <span style="top:40px"></span><span style="top:69px"></span><span style="top:98px"></span>
    </div>
  </header>

  <nav class="nav">
    <div class="nav-item">Unternehmen<svg viewBox="0 0 100 100"><circle cx="50" cy="50" r="45" fill="none" stroke="#fff" stroke-width="6"/><path d="M26 50h46M54 32l18 18-18 18" fill="none" stroke="#fff" stroke-width="6" stroke-linecap="round" stroke-linejoin="round"/></svg></div>
    <div class="nav-item">Leistungen<svg viewBox="0 0 100 100"><circle cx="50" cy="50" r="45" fill="none" stroke="#fff" stroke-width="6"/><path d="M26 50h46M54 32l18 18-18 18" fill="none" stroke="#fff" stroke-width="6" stroke-linecap="round" stroke-linejoin="round"/></svg></div>
    <div class="nav-item">Referenzen<svg viewBox="0 0 100 100"><circle cx="50" cy="50" r="45" fill="none" stroke="#fff" stroke-width="6"/><path d="M26 50h46M54 32l18 18-18 18" fill="none" stroke="#fff" stroke-width="6" stroke-linecap="round" stroke-linejoin="round"/></svg></div>
    <div class="nav-item">Stellenangebote<svg viewBox="0 0 100 100"><circle cx="50" cy="50" r="45" fill="none" stroke="#fff" stroke-width="6"/><path d="M26 50h46M54 32l18 18-18 18" fill="none" stroke="#fff" stroke-width="6" stroke-linecap="round" stroke-linejoin="round"/></svg></div>
  </nav>

  <h2 class="section-title">UNSERE LEISTUNGEN</h2>
  <p class="intro">Wir haben 180 Jahre Erfahrung im Stahl- und Brückenbau.</p>

  <article class="card blue" style="top:1494px">
    <div class="card-head"><div class="icon-tile"><div class="mark" role="img" aria-label="Baustellen-Symbol"></div></div><h3 class="card-title">Brücken</h3></div>
    <div class="divider"></div>
    <p class="card-text">Die Fertigung umfasst unter<br>anderem Brücken mit orthotroper<br>Platte, Bogen-, Fachwerk-,<br>Schrägseil- und Stahlverbundbrücken.</p>
  </article>

  <article class="card dark" style="top:2229px">
    <div class="card-head"><div class="icon-tile"><div class="mark" role="img" aria-label="Baustellen-Symbol"></div></div><h3 class="card-title">VF-Träger</h3></div>
    <div class="divider"></div>
    <p class="card-text">Die Fertigung umfasst unter<br>anderem Brücken mit orthotroper<br>Platte, Bogen-, Fachwerk-,<br>Schrägseil- und Stahlverbundbrücken.</p>
  </article>

  <article class="card dark" style="top:2968px">
    <div class="card-head"><div class="icon-tile"><div class="mark" role="img" aria-label="Baustellen-Symbol"></div></div><h3 class="card-title">Sonderstahlbau</h3></div>
    <div class="divider"></div>
    <p class="card-text">Die Fertigung umfasst unter<br>anderem Brücken mit orthotroper<br>Platte, Bogen-, Fachwerk-,<br>Schrägseil- und Stahlverbundbrücken.</p>
  </article>
</body>
</html>
```